Eye-grabbing water bottle design

Dears,
We are a new table water manufacturer and we want a new design for our 1.5L water bottle. The brand name is "Dunmora" and the bottle will be transparent. The label will be encircling the bottle and will be made of foil - 70mm wide and 290mm long.

I. Requirements

The bottle:
1) has to be 302.7mm in height
2) has to have a diameter in the body of about 93mm with its respective narrowing near the neck.
3) there has to be something like a narrowing (in the shape of a ring) in the middle part of the bottle (for ergenomic purposes) so it is easier for people to hold it.
4) we want it to have edges/bumps, because we are using a pre-form with smaller weight. This "roughness" is necessary so that the bottle is stronger and more resistent to pressure. In other words, we do not want a bottle flat and smooth like silk.
5) also, since our brand is "Dunmora", we want some of those bumps/edges/curves to be in the shape of an iceberg.
6) you can use curves, arcs, angles - whatever you think it is going to make the bottle perfect.

7) the purpose of the design is to grab the eye, so customers in the retail shops stretch their hand to grab our bottle, not the one of the competitors which is right next to ours on the shelf.
8) the design has to communicate freshness, pureness and sweet taste (like the iceberg itself). Most important of all - it has to be visually salient and simple at the same time, and be able to build brand awareness.

9) anything else you can think of which will make customers choose our water when making their purchasing decisions (:

P.S. The quality and taste of our water is very good, so the design has to also match our quality
Updates

Hello all creative people, 1. Please, read carefully the project's brief so you understand exactly what are our needs. 2. Please, submit ONLY ONE deisgn of a BOTTLE, NOT of a LABEL. We are looking for a bottle design. Thank you very much and keep up the good work! Best Regards,

Target Market(s)

Our target includes all customers from all income-levels segment.

Industry/Entity Type

Water Company

Requirements
Must have
• to be visually salient, elegant and simple at the same time.
Please see project description for more details
Nice to have
• Please see project description for more details

```html
<!DOCTYPE html>
<html lang="en">
<head>
<meta charset="utf-8">
<title>Dunmora water – 1.5 l bottle</title>
<link href="https://fonts.googleapis.com/css2?family=Lora:wght@400&display=swap" rel="stylesheet">
<style>
  :root {
    --backdrop: #d3e0f1;
    --cap: #7f9ed6;
    --cap-shade: #5b7cbf;
    --plastic-edge: #c5d0df;
    --ridge: #b9c5d6;
    --label-base: #eef2f9;
    --ice-deep: #8ea6d2;
    --ice-light: #dfe7f4;
    --label-ink: #4a5682;
  }
  html, body {
    margin: 0;
    padding: 0;
    width: 1200px;
    height: 938px;
    overflow: hidden;
    background: var(--backdrop);
  }
  .canvas { display: block; width: 1200px; height: 938px; }
  .label-text { font-family: "Lora", serif; font-weight: 400; fill: var(--label-ink); }
</style>
</head>
<body>
<svg class="canvas" viewBox="0 0 1200 938" xmlns="http://www.w3.org/2000/svg">
  <defs>
    <linearGradient id="plasticShade" x1="0" x2="1" y1="0" y2="0">
      <stop offset="0" stop-color="#d9e1ec"/>
      <stop offset="0.5" stop-color="#f3f6fa"/>
      <stop offset="1" stop-color="#d9e1ec"/>
    </linearGradient>
    <linearGradient id="labelArt" x1="0" y1="0" x2="0" y2="1">
      <stop offset="0" stop-color="var(--ice-deep)"/>
      <stop offset="0.25" stop-color="var(--ice-light)"/>
      <stop offset="0.55" stop-color="#f6f8fc"/>
      <stop offset="0.75" stop-color="#cbd8ee"/>
      <stop offset="1" stop-color="var(--ice-light)"/>
    </linearGradient>
  </defs>

  <g class="bottle">
    <rect class="bottle-cap" x="563" y="68" width="75" height="30" rx="4" fill="var(--cap)"/>
    <rect class="cap-ring" x="558" y="96" width="85" height="7" rx="2" fill="var(--cap-shade)"/>

    <path class="bottle-body" fill="url(#plasticShade)" stroke="var(--plastic-edge)" stroke-width="1.5"
      d="M572 103 L629 103 L631 130
         C633 165 700 210 705 270
         L707 470 C709 478 709 484 706 488
         L706 738 C710 748 711 760 708 770
         L710 860 C710 880 700 888 680 888
         L520 888 C500 888 492 880 492 860
         L494 770 C491 760 492 748 496 738
         L496 488 C493 484 493 478 495 470
         L497 270 C502 210 568 165 570 130 Z"/>

    <g class="shoulder-ridges" fill="none" stroke="var(--ridge)" stroke-width="3" stroke-linecap="round">
      <path d="M530 200 L601 245 L672 200"/>
      <path d="M515 255 L601 300 L687 255"/>
      <path d="M510 310 L601 355 L692 310"/>
      <path d="M510 365 L601 410 L692 365"/>
    </g>

    <g class="grip-rings" fill="none" stroke="var(--ridge)" stroke-width="3">
      <path d="M496 770 C540 755 560 760 601 770 C642 760 662 755 706 770"/>
      <path d="M494 800 C540 785 560 790 601 800 C642 790 662 785 708 800"/>
      <path d="M494 830 C540 815 560 820 601 830 C642 820 662 815 708 830"/>
    </g>
  </g>

  <g class="label">
    <rect class="label-band" x="496" y="486" width="210" height="252" fill="var(--label-base)"/>
    <rect class="label-artwork" x="496" y="486" width="210" height="252" fill="url(#labelArt)"
      role="img" aria-label="Faceted ice pattern with an iceberg floating in water and rising bubbles"/>
    <text class="label-text brand-name" x="601" y="600" font-size="38" text-anchor="middle">Dunmora</text>
    <text class="label-text volume" x="684" y="717" font-size="15" text-anchor="end">1.5 l</text>
  </g>
</svg>
</body>
</html>
```